Label for Dog Nourishing CBD Balm

Dear Designers,

We are looking for a packaging expert to design our new Hydrating Balm for dogs which contain a relaxing hemp extract (CBD). The product is intended to be massaged on the dog’s paws to make them softer and promote the animal’s well-being :)

Our company is already selling various relaxing cat & dog products, and we would like this new design to reflect the same "style & feeling" as our current products (see attached ZIP file).

Technical aspects:
- The packaging is a 40ml aluminium jar (58mm x 23mm).
- We are looking to design 2 separate labels (one for the front, one for the back)
- The label dimensions should be : 50mm x 50mm
- Please follow technical guidelines from printer (see ZIP file).

Design aspects:
- The design should be compatible with our brand identity (i.e. fluffly, pure, relaxing, positive, clean & natural).
- People should understand what the product "is" and what the product "does" simply from looking at the design.
- The actual balm is white/yellow in color.
- Soft/rounded shapes are preferred.
- Please use our brand's colors (see typo & colors in ZIP file)
- Please use our brand's fonts (see typo & colors in ZIP file)
- Please use our company logo (see ZIP file).
- The design also needs to convey a strong sense of professionalism as we are an animal "healthcare" brand.
- If you want to include a dog picture, we would prefer you to use a picture of our official brand ambassador (see ZIP file).
- Only original work (no plagiarism will be accepted).

Please don't hesitate to send us a message if you have any questions about the brand, the product or the design requirements.

We look forward to seeing your designs & working on this together !

Thanks & regards,
Marcus

Target Market(s)

Dog owners

Font styles to use
Other font styles liked:
• See ZIP file

Requirements
Must have
• Brand fonts (see typo & colors in ZIP file)
Brand colors (see typo & colors in ZIP file)

```html
<!DOCTYPE html>
<html lang="en">
<head>
<meta charset="utf-8">
<title>VerdaBalm Soothing Balm – Lid Label</title>
<link rel="stylesheet" href="https://fonts.googleapis.com/css2?family=Arvo&family=Oswald:wght@500&family=Quicksand:wght@300&family=Lato:wght@400;700&display=swap">
<style>
  :root {
    --teal: #3b9e7e;
    --teal-soft: #7cc0a8;
    --ink: #1f2a22;
    --paper: #ffffff;
    --backdrop: #505050;
  }
  html, body {
    margin: 0;
    padding: 0;
    width: 819px;
    height: 1200px;
    overflow: hidden;
    background: var(--backdrop);
  }
  .label {
    display: block;
    width: 819px;
    height: 1200px;
  }
  .label__paper { fill: var(--paper); }
  .label__ring--thin { fill: none; stroke: var(--teal); stroke-width: 3; }
  .label__ring--bold { fill: none; stroke: var(--teal); stroke-width: 10; }
  .label__ground { fill: url(#ground-tone); }
  .label__pets { fill: url(#pets-tone); }
  .product-line {
    font-family: "Quicksand", sans-serif;
    font-weight: 300;
    font-size: 50px;
    letter-spacing: 9px;
    fill: var(--teal);
  }
  .brand-name {
    font-family: "Arvo", serif;
    font-size: 41px;
    fill: var(--ink);
  }
  .brand-mark { fill: none; stroke: var(--ink); stroke-width: 3; }
  .brand-tagline {
    font-family: "Arvo", serif;
    font-size: 16px;
    letter-spacing: 0.5px;
    fill: var(--teal);
  }
  .title-rule { stroke: var(--teal); stroke-width: 2.5; }
  .product-title {
    font-family: "Oswald", sans-serif;
    font-weight: 500;
    font-size: 50px;
    fill: var(--teal);
  }
  .benefits {
    font-family: "Lato", sans-serif;
    font-size: 18px;
    fill: var(--ink);
  }
  .benefits__divider { fill: var(--teal); }
  .specs {
    font-family: "Lato", sans-serif;
    font-weight: 700;
    font-size: 12px;
    fill: var(--teal);
  }
</style>
</head>
<body>
<svg class="label" viewBox="0 0 819 1200" xmlns="http://www.w3.org/2000/svg" role="img" aria-label="VerdaBalm soothing balm lid label">
  <defs>
    <clipPath id="inner-disc">
      <circle cx="409.5" cy="600" r="292"/>
    </clipPath>
    <linearGradient id="ground-tone" x1="0" y1="0" x2="0" y2="1">
      <stop offset="0" stop-color="#3b9e7e"/>
      <stop offset="1" stop-color="#45a886"/>
    </linearGradient>
    <linearGradient id="pets-tone" x1="0" y1="0" x2="0" y2="1">
      <stop offset="0" stop-color="#7cc0a8"/>
      <stop offset="1" stop-color="#3b9e7e"/>
    </linearGradient>
    <path id="product-arc" d="M 180 600 A 229.5 229.5 0 0 1 639 600"/>
  </defs>

  <circle class="label__paper" cx="409.5" cy="600" r="340"/>
  <circle class="label__ring--thin" cx="409.5" cy="600" r="315"/>
  <circle class="label__ring--bold" cx="409.5" cy="600" r="297"/>

  <rect class="label__ground" x="100" y="782" width="620" height="140" clip-path="url(#inner-disc)" role="img" aria-label="Green ground band scattered with white paw prints"/>

  <text class="product-line"><textPath href="#product-arc" startOffset="50%" text-anchor="middle">VerdaBalm<tspan font-size="22" letter-spacing="2" dy="-6">™</tspan></textPath></text>

  <circle class="brand-mark" cx="287" cy="510" r="8"/>
  <text class="brand-name" x="414" y="524" text-anchor="middle">VERDALIA</text>
  <text class="brand-tagline" x="517" y="550" text-anchor="end">For Animals</text>

  <line class="title-rule" x1="266" y1="567" x2="553" y2="567"/>
  <text class="product-title" x="409.5" y="617" text-anchor="middle" textLength="286" lengthAdjust="spacingAndGlyphs">SOOTHING BALM</text>
  <line class="title-rule" x1="266" y1="623" x2="553" y2="623"/>

  <text class="benefits" x="409.5" y="654" text-anchor="middle">REPAIR <tspan class="benefits__divider">|</tspan> NOURISH <tspan class="benefits__divider">|</tspan> PROTECT</text>
  <text class="specs" x="409.5" y="682" text-anchor="middle">40g | CBD 250mg | 0% THC</text>

  <rect class="label__pets" x="328" y="698" width="164" height="86" rx="12" role="img" aria-label="Silhouette of a dog and a cat sitting nose to nose"/>
</svg>
</body>
</html>
```